Need business card design for a confectionery company specializing in chocolates. Would like to see designs that use chocolate brown background and lime green wording and logo. Logo preferably chocolate-related.

Target Market(s)

Corporate, Gifts & Occasions, Hotels, Supermarkets, Parties, Events, Weddings

Industry/Entity Type

Food Production

Contact Information for Business Card

Velbrook Confectionery (company name on front of card in lime green)
with words beneath company name saying "chocolates for every occassion" (in lime green in lower case)

Font styles to use
Script

Colors
acd037

Requirements
Must have
• Front of card: Brown background
• Back of card: White background
• Email address on back of card: Info@velbrook.example.zw
• Cellphone number on back of card: 0771 392 615, 0773 581 246
• Address on back of card: 8 Tarnby Close, Marlow Rise, Harare
• ALL WRITING ON BACK OF CARD IN BLACK

```html
<!DOCTYPE html>
<html lang="en">
<head>
<meta charset="utf-8">
<title>Velbrook Confectionery – Business Card</title>
<link rel="stylesheet" href="https://fonts.googleapis.com/css2?family=Kaushan+Script&family=Arimo:wght@400&display=swap">
<style>
  :root {
    --backdrop: #fde5b6;
    --card-white: #ffffff;
    --chocolate: #512a18;
    --lime: #c6d30b;
    --ink: #2b2321;
    --shadow: rgba(110, 80, 30, 0.28);
  }
  * { margin: 0; padding: 0; box-sizing: border-box; }
  html, body { width: 1200px; height: 1200px; overflow: hidden; }
  body {
    background: var(--backdrop);
    position: relative;
    font-family: "Arimo", Arial, sans-serif;
  }
  .card {
    position: absolute;
    border-radius: 30px;
    overflow: hidden;
    box-shadow: 0 18px 30px var(--shadow);
  }
  /* Contact side */
  .card--contact {
    left: 216px; top: 99px; width: 760px; height: 432px;
    background: var(--card-white);
  }
  .holder-name {
    position: absolute; left: 62px; top: 72px;
    font-family: "Kaushan Script", cursive;
    font-size: 58px; color: var(--ink);
    letter-spacing: 1px;
  }
  .contact-band {
    position: absolute; left: 62px; top: 169px;
    width: 64px; height: 300px;
    background: var(--lime);
    border-radius: 32px 32px 0 0;
  }
  .contact-row {
    position: absolute; left: 72px;
    display: flex; align-items: center; gap: 26px;
    color: var(--ink);
  }
  .contact-row svg { width: 44px; height: 44px; flex: none; }
  .contact-row--email { top: 190px; font-size: 23px; }
  .contact-row--phone { top: 269px; font-size: 19px; letter-spacing: 0.6px; }
  .contact-row--address { top: 346px; font-size: 20px; }
  .brand-mark {
    position: absolute; right: 20px; top: 60px;
    display: flex; flex-direction: column; align-items: center; gap: 8px;
  }
  .brand-mark__dot {
    width: 70px; height: 70px; border-radius: 50%;
    background: var(--lime);
  }
  .brand-mark__name {
    font-family: "Kaushan Script", cursive;
    font-size: 34px; color: var(--lime);
  }
  /* Brand side */
  .card--brand {
    left: 213px; top: 617px; width: 761px; height: 431px;
    background: var(--chocolate);
    text-align: center;
  }
  .brand-dot {
    position: absolute; left: 330px; top: 65px;
    width: 100px; height: 100px; border-radius: 50%;
    background: var(--lime);
  }
  .company-name {
    position: absolute; left: 0; right: 0; top: 192px;
    font-family: "Kaushan Script", cursive;
    font-size: 50px; color: var(--lime);
    letter-spacing: 1px;
  }
  .tagline {
    position: absolute; left: 0; right: 0; top: 257px;
    font-size: 24px; color: var(--lime);
  }
</style>
</head>
<body>
  <section class="card card--contact">
    <h1 class="holder-name">Rudo Marwick</h1>
    <div class="contact-band"></div>

    <div class="contact-row contact-row--email">
      <svg viewBox="0 0 44 44" aria-hidden="true">
        <circle cx="22" cy="22" r="22" fill="var(--ink)"/>
        <rect x="11" y="14" width="22" height="16" rx="1.5" fill="var(--lime)"/>
        <path d="M11.5 15 L22 23.5 L32.5 15" fill="none" stroke="var(--ink)" stroke-width="1.8"/>
      </svg>
      <span>Info@velbrook.example.zw</span>
    </div>

    <div class="contact-row contact-row--phone">
      <svg viewBox="0 0 44 44" aria-hidden="true">
        <circle cx="22" cy="22" r="22" fill="var(--ink)"/>
        <path d="M15 11.5c1-.8 2.3-.6 3 .4l2.2 3.3c.6.9.4 2.1-.4 2.8l-1.5 1.2c1 2.5 3 4.6 5.5 5.6l1.2-1.5c.7-.8 1.9-1 2.8-.4l3.3 2.2c1 .7 1.2 2 .4 3l-1.4 1.7c-1 1.2-2.7 1.6-4.2 1-6.3-2.5-11-7.3-13.5-13.5-.6-1.5-.2-3.2 1-4.2z" fill="var(--lime)"/>
      </svg>
      <span>0771 392 615, 0773 581 246</span>
    </div>

    <div class="contact-row contact-row--address">
      <svg viewBox="0 0 44 44" aria-hidden="true">
        <circle cx="22" cy="22" r="22" fill="var(--ink)"/>
        <path d="M22 9c-5 0-8.5 3.8-8.5 8.4 0 6 8.5 16.6 8.5 16.6s8.5-10.6 8.5-16.6C30.5 12.8 27 9 22 9z" fill="none" stroke="var(--lime)" stroke-width="2.4"/>
        <circle cx="22" cy="17.5" r="3.2" fill="var(--lime)"/>
      </svg>
      <span>8 Tarnby Close, Marlow Rise, Harare</span>
    </div>

    <div class="brand-mark">
      <div class="brand-mark__dot"></div>
      <span class="brand-mark__name">Velbrook</span>
    </div>
  </section>

  <section class="card card--brand">
    <div class="brand-dot"></div>
    <h2 class="company-name">Velbrook Confectionery</h2>
    <p class="tagline">chocolates for every occassion</p>
  </section>
</body>
</html>
```